SPIRIT ALBA/COPPERKNOLL DISTILLERY

DOUBLE SIDED BUSINESS CARD ONE SIDE FOR WWW.SPIRITALBA-EXAMPLE.ORG AND ONE SIDE FOR COPPERKNOLL DISTILLERY ARTWORK FOR WEBSITE IS ATTACHED

1)
GORDON PRICE CEO
SPIRIT ALBA
Office 4 Meridian Court
17 Larch Terrace
Glasgow
Scotland, G5 2QX
W:WWW.SPIRITALBA-EXAMPLE.ORG
E:GORDON@SPIRITALBA-EXAMPLE.ORG
T:+44 7412 559031

2)
GORDON PRICE CEO
COPPERKNOLL DISTILLERY
Building 148, Havenpark Rozendaal,
3e Berkenlaan, Katwijk, 2231KT

W: WWW.copperknolldistillery-example.nl
E: GORDON@copperknolldistillery-example.nl
T:+44 7412 559031

1)
Petra Vosberg DIRECTOR
SPIRIT ALBA
Office 4 Meridian Court
17 Larch Terrace
Glasgow
Scotland, G5 2QX
W:WWW.SPIRITALBA-EXAMPLE.ORG
E:Petra@SPIRITALBA-EXAMPLE.ORG
T:+31 6 58173420

2)
PETRA VOSBERG DIRECTOR
COPPERKNOLL DISTILLERY

E: petra@copperknolldistillery-example.nl
T:+31 6 58173420

```html
<!DOCTYPE html>
<html lang="en">
<head>
<meta charset="utf-8">
<title>Spirit Alba / Copperknoll Distillery – Business Card</title>
<link rel="stylesheet" href="https://fonts.googleapis.com/css2?family=Arimo:wght@400;700&display=swap">
<style>
  :root {
    --stage: #141414;
    --card-dark: #1e1a17;
    --card-light: #ffffff;
    --gold: #c9a13e;
    --gold-deep: #b8902f;
    --ink: #2b2b2b;
    --white: #ffffff;
  }
  * { box-sizing: border-box; margin: 0; padding: 0; }
  html, body { width: 1200px; height: 900px; overflow: hidden; }
  body {
    background: var(--stage);
    font-family: "Arimo", Arial, sans-serif;
    display: flex;
    flex-direction: column;
    align-items: center;
    justify-content: center;
    gap: 36px;
  }
  .card {
    position: relative;
    width: 700px;
    height: 400px;
    overflow: hidden;
    box-shadow: 0 10px 30px rgba(0,0,0,.5);
  }
  .card--distillery { background: var(--card-dark); color: var(--white); }
  .card--alba { background: var(--card-light); color: var(--ink); }

  .brand {
    position: absolute;
    left: 0; right: 0;
    top: 92px;
    display: flex;
    align-items: center;
    justify-content: center;
    gap: 14px;
    padding-left: 120px;
  }
  .brand-dot {
    width: 18px; height: 18px;
    border-radius: 50%;
    background: var(--gold);
  }
  .brand-name {
    font-weight: 700;
    font-size: 36px;
    letter-spacing: 2px;
  }
  .card--distillery .brand-name { color: var(--white); font-size: 32px; }
  .card--alba .brand-name { color: var(--gold); font-size: 44px; letter-spacing: 4px; }

  .details {
    position: absolute;
    left: 0; right: 0;
    top: 200px;
    display: flex;
    align-items: center;
    justify-content: center;
    padding-left: 40px;
  }
  .person {
    text-align: right;
    padding-right: 18px;
  }
  .person-name {
    font-weight: 700;
    font-size: 26px;
    color: var(--gold);
    letter-spacing: .5px;
  }
  .person-role {
    font-size: 17px;
    margin-top: 2px;
  }
  .divider {
    width: 1.5px;
    height: 74px;
    background: currentColor;
    opacity: .8;
  }
  .contacts {
    list-style: none;
    padding-left: 18px;
    font-size: 13.5px;
    line-height: 23px;
  }
  .contacts li { display: flex; align-items: center; gap: 9px; }
  .contacts svg { width: 14px; height: 14px; flex: none; }
  .card--distillery .contacts svg { fill: var(--gold); }
  .card--alba .contacts svg { fill: var(--gold); }

  .address-band {
    position: absolute;
    left: 0; right: 0; bottom: 0;
    height: 64px;
    background: var(--gold);
    color: var(--white);
    display: flex;
    align-items: center;
    justify-content: center;
    font-size: 16px;
    letter-spacing: .3px;
  }
  .card--distillery .address-band { background: linear-gradient(90deg, var(--gold-deep), var(--gold)); }
</style>
</head>
<body>

  <section class="card card--distillery" aria-label="Copperknoll Distillery side">
    <div class="brand">
      <span class="brand-dot"></span>
      <span class="brand-name">COPPERKNOLL DISTILLERY</span>
    </div>
    <div class="details">
      <div class="person">
        <p class="person-name">GORDON PRICE</p>
        <p class="person-role">CEO</p>
      </div>
      <div class="divider"></div>
      <ul class="contacts">
        <li><svg viewBox="0 0 16 16"><path d="M3.6 1.5l2.4 2.8-1.3 1.6c.9 2 2.4 3.5 4.4 4.4l1.6-1.3 2.8 2.4-1.3 2.4C7 13.6 2.4 9 1.2 2.8z"/></svg>+44 7412 559031</li>
        <li><svg viewBox="0 0 16 16"><path d="M1 3h14v10H1z M2 4l6 5 6-5" stroke="#1e1a17" stroke-width="1"/></svg>GORDON@copperknolldistillery-example.nl</li>
        <li><svg viewBox="0 0 16 16"><circle cx="8" cy="8" r="7"/><path d="M1 8h14M8 1c-3 3-3 11 0 14M8 1c3 3 3 11 0 14" stroke="#1e1a17" stroke-width="1" fill="none"/></svg>WWW.copperknolldistillery-example.nl</li>
      </ul>
    </div>
    <p class="address-band">Building 148, Havenpark Rozendaal, 3e Berkenlaan, Katwijk, 2231KT</p>
  </section>

  <section class="card card--alba" aria-label="Spirit Alba side">
    <div class="brand">
      <span class="brand-dot"></span>
      <span class="brand-name">SPIRIT ALBA</span>
    </div>
    <div class="details">
      <div class="person">
        <p class="person-name">GORDON PRICE</p>
        <p class="person-role">CEO</p>
      </div>
      <div class="divider"></div>
      <ul class="contacts">
        <li><svg viewBox="0 0 16 16"><path d="M3.6 1.5l2.4 2.8-1.3 1.6c.9 2 2.4 3.5 4.4 4.4l1.6-1.3 2.8 2.4-1.3 2.4C7 13.6 2.4 9 1.2 2.8z"/></svg>+44 7412 559031</li>
        <li><svg viewBox="0 0 16 16"><path d="M1 3h14v10H1z M2 4l6 5 6-5" stroke="#ffffff" stroke-width="1"/></svg>GORDON@SPIRITALBA-EXAMPLE.ORG</li>
        <li><svg viewBox="0 0 16 16"><circle cx="8" cy="8" r="7"/><path d="M1 8h14M8 1c-3 3-3 11 0 14M8 1c3 3 3 11 0 14" stroke="#ffffff" stroke-width="1" fill="none"/></svg>WWW.SPIRITALBA-EXAMPLE.ORG</li>
      </ul>
    </div>
    <p class="address-band">Office 4 Meridian Court, 17 Larch Terrace, Glasgow, Scotland, G5 2QX</p>
  </section>

</body>
</html>
```